Morning Harvest Psalm Journal for the Weary Traveler on the Narrow Road

This is not an Eastern meditation method. No images or themes from guru style or Eastern meditations from Hinduism or Buddhism will work. This is a Biblical Christian-based method. Some sort of Divine Light from Heaven may be the look. Some "ancient scroll" for the title to be written in may work.

```html
<!DOCTYPE html>
<html lang="en">
<head>
<meta charset="UTF-8">
<title>Morning Harvest Psalm Journal – Cover</title>
<link href="https://fonts.googleapis.com/css2?family=Permanent+Marker&family=Libre+Baskerville&display=swap" rel="stylesheet">
<style>
  :root {
    --page-bg: #e4e4e4;
    --sky-top: #9c4449;
    --sky-upper: #d9675a;
    --sky-mid: #f1946c;
    --sky-glow: #fde9cb;
    --sky-low: #f6b79a;
    --dusk-ground: #150808;
    --title-ink: #0f2252;
    --subtitle-ink: #1b1414;
  }
  * { margin: 0; padding: 0; box-sizing: border-box; }
  html, body {
    width: 1200px;
    height: 800px;
    overflow: hidden;
    background: var(--page-bg);
  }
  .canvas {
    position: relative;
    width: 1200px;
    height: 800px;
  }
  .cover {
    position: absolute;
    left: 350px;
    top: 17px;
    width: 500px;
    height: 766px;
    overflow: hidden;
  }
  .cover-sky {
    position: absolute;
    inset: 0;
    background:
      radial-gradient(ellipse 60% 45% at 55% 62%, var(--sky-glow) 0%, rgba(253,233,203,0.75) 35%, rgba(253,233,203,0) 75%),
      linear-gradient(to bottom,
        var(--sky-top) 0%,
        var(--sky-upper) 18%,
        var(--sky-mid) 38%,
        var(--sky-glow) 60%,
        var(--sky-low) 82%,
        #c98475 89%,
        var(--dusk-ground) 95%,
        var(--dusk-ground) 100%);
  }
  .cover-text {
    position: absolute;
    inset: 0;
    text-align: center;
  }
  .book-title {
    position: absolute;
    top: 118px;
    left: 0;
    right: 0;
    padding-left: 40px;
    font-family: "Permanent Marker", cursive;
    font-weight: 400;
    font-size: 66px;
    line-height: 108px;
    color: var(--title-ink);
    letter-spacing: 1px;
  }
  .book-title span { display: block; }
  .book-subtitle {
    position: absolute;
    top: 532px;
    left: 0;
    right: 0;
    padding-left: 0;
    font-family: "Libre Baskerville", serif;
    font-weight: 400;
    font-size: 24px;
    line-height: 36px;
    color: var(--subtitle-ink);
    text-transform: uppercase;
  }
  .book-subtitle span { display: block; }
</style>
</head>
<body>
  <main class="canvas">
    <section class="cover">
      <div class="cover-sky" role="img" aria-label="Photograph of a glowing sunset sky with rays of light bursting through clouds above a dark silhouette of rooftops"></div>
      <div class="cover-text">
        <h1 class="book-title">
          <span>Morning</span>
          <span>Harvest</span>
          <span>Psalm</span>
          <span>Journal</span>
        </h1>
        <p class="book-subtitle">
          <span>For the Weary Traveler</span>
          <span>on the Narrow</span>
          <span>Road</span>
        </p>
      </div>
    </section>
  </main>
</body>
</html>
```